International travel site frontpage redesign

We sell tours to Scandinavia through our website www.velmora-journeys.com. The website has become a bit old fashioned and we are in the process of making the website responsive. As you can see from the attached pictures the website will be wider with the responsive design, and our current design does not fit anymore.

Here is what we are looking for:
- A website that reflects a trustworthy and quality oriented company.
- Making the website more modern looking, but still recognisable (we want to keep the colours).
- keeping in mind that the age group of our customers are from 20-80 years old (most in their 60s).
- We want to remove the popular tours part and are instead looking to replace this with picture boxes the following subjects Scandinavia Specialist, Special Offers, Contact, Norway (or Norway Tours), Sweden (or Sweden Tours), Iceland (or Iceland Tours), Combination Tours. Possibly also Lapland, Winter, Northern Lights, Fjords and Capitals. Some of these categories can be smaller or perhaps half boxes; i.e. Winter and Northern lights in one. If we end up with four boxes per line perhaps we could add a social media box next to the three first ones.
- The above means that the left hand meny with Norway Tours, Sweden Tours etc will be redundant.
- we will add another line to the search Box (on the top): Destinations
- The top menu will have the same categories, but we need to add languages as the website will be in English and German.
- The footer must be changed
- We can take away the box to the right where it says "your window to booking the best of our world"

Reason: One of the decission makers had to go away on business last minute.

Target Market(s)

Travelling to Scandinavia is not low cost, so the website needs to appeal to those that can afford to travel to our destination.
The age group of our customers are from 20-80 years old (most in their 60s).

Industry/Entity Type

Travel

Number of Pages Required

1 page

Requirements
Should not have
• Flashy or cheap looking special offers...

```html
<!DOCTYPE html>
<html lang="en">
<head>
<meta charset="utf-8">
<title>Velmora Journeys – Tours to Scandinavia</title>
<link rel="stylesheet" href="https://fonts.googleapis.com/css2?family=Lato:wght@400;700&display=swap">
<style>
  :root {
    --page-bg: #ffffff;
    --header-bg: #f6f6f6;
    --header-line: #e2e2e2;
    --nav-text: #555555;
    --nav-active-bg: #e6e6e6;
    --nav-active-line: #d2d2d2;
    --brand-text: #5a5a5a;
    --accent: #d9474a;
    --accent-dark: #a81c1f;
    --title-text: #3d3d3d;
    --lead-text: #5d5d5d;
    --button-text: #ffffff;
  }
  * { box-sizing: border-box; margin: 0; padding: 0; }
  html, body {
    width: 1200px; height: 516px; overflow: hidden;
    background: var(--page-bg);
    font-family: "Lato", Arial, sans-serif;
  }
  .site { position: relative; width: 1200px; height: 516px; overflow: hidden; }

  .site-header {
    position: absolute; left: 0; top: 0; width: 1200px; height: 86px;
    background: var(--header-bg);
    border-bottom: 1px solid var(--header-line);
  }
  .brand {
    position: absolute; left: 98px; top: 28px; height: 30px;
    display: flex; align-items: center; gap: 12px;
    color: var(--brand-text);
    font-size: 22px; font-weight: 400; letter-spacing: 1.5px;
    text-transform: uppercase; text-decoration: none;
  }
  .brand-mark { width: 14px; height: 14px; background: var(--accent-dark); }

  .main-nav { position: absolute; left: 477px; top: 27px; display: flex; }
  .main-nav a {
    display: block; height: 31px; line-height: 31px;
    padding: 0 12px; margin-right: 26px;
    font-size: 14px; color: var(--nav-text);
    text-decoration: none; text-transform: uppercase;
    border-radius: 3px;
  }
  .main-nav a.is-active {
    text-transform: none;
    background: var(--nav-active-bg);
    border: 1px solid var(--nav-active-line);
    line-height: 29px;
  }

  .hero {
    position: absolute; left: 92px; top: 104px; width: 1013px; height: 412px;
    overflow: hidden;
  }
  .hero-photo {
    position: absolute; inset: 0;
    background:
      linear-gradient(180deg,
        #2b3a5e 0%, #6a3f66 18%, #b7586a 32%, #f08a5a 42%, #f6c56a 47%,
        #2a2f45 52%, #3b4663 62%, #c58a5c 70%, #d9a46a 74%,
        #4d7fa6 82%, #2f5a80 100%);
  }
  .hero-content {
    position: absolute; left: 0; top: 158px; width: 100%;
    text-align: center;
  }
  .hero-title {
    font-size: 38px; font-weight: 400; color: var(--title-text);
    line-height: 44px;
  }
  .hero-title .dot { color: var(--accent); }
  .hero-lead {
    margin-top: 12px;
    font-size: 14px; line-height: 27px; color: var(--lead-text);
  }
  .hero-button {
    display: inline-block; margin-top: 42px;
    width: 104px; height: 35px; line-height: 35px;
    background: var(--accent); color: var(--button-text);
    font-size: 13px; text-transform: uppercase; text-decoration: none;
    border-radius: 3px;
  }
</style>
</head>
<body>
<div class="site">
  <header class="site-header">
    <a class="brand" href="#"><span class="brand-mark"></span>Velmora Journeys</a>
    <nav class="main-nav">
      <a class="is-active" href="#">Home</a>
      <a href="#">Fjords</a>
      <a href="#">Capitals</a>
      <a href="#">Cruises</a>
      <a href="#">Winter</a>
      <a href="#">Pictures</a>
    </nav>
  </header>

  <section class="hero">
    <div class="hero-photo" role="img" aria-label="Photo of snowy mountain peaks above a calm harbour with red fishing cabins at sunset in the Lofoten Islands"></div>
    <div class="hero-content">
      <h1 class="hero-title">Lofoten Island<span class="dot">.</span></h1>
      <p class="hero-lead">Lorem ipsum dolor sit amet, consectetur adipiscing elit sed do eiusmod<br>ut enim ad minim veniam quis nostrud</p>
      <a class="hero-button" href="#">More info</a>
    </div>
  </section>
</div>
</body>
</html>
```